Acupuncture Medspa needs a business card design

I need a business card design that looks professional, has a spa-like quality and can offer a promo on the back. Initial promo is "First session free". The tagline of NeedleNook is: Refresh, Restore, Rejuvenate.

NeedleNook is a membership-based acupuncture medspa that offers acupuncture, cupping, and herbal therapies. Members choose between the "Refresh" membership which is for stress relief, or "Restore" which is for treating health conditions, and lastly "Rejuvenate" which is for natural facial enhancement.

Industry/Entity Type

Health And Wellness

Contact Information for Business Card

Coral Haskins, MAC, L.Ac.
612-555-0193
www.needlenook-example.com

Font styles to use
Serif
Sans Serif

Colors

Designer to choose colors to be used in the design.

Requirements
Must have
• The project must have NeedleNook logo, promo on the back, and contact information
Nice to have
• I would like to see the colors of the logo used.

```html
<!DOCTYPE html>
<html lang="en">
<head>
<meta charset="utf-8">
<title>NeedleNook Business Card</title>
<link href="https://fonts.googleapis.com/css2?family=Lato:wght@400;700;900&family=Montserrat:wght@600&display=swap" rel="stylesheet">
<style>
  :root {
    --teal: #008a80;
    --teal-soft: #12998f;
    --brown: #3d2419;
    --ink: #2b2b2b;
    --paper: #ffffff;
    --backdrop: #e9e9e9;
  }
  html, body {
    margin: 0;
    padding: 0;
    width: 1200px;
    height: 895px;
    overflow: hidden;
    background: var(--backdrop);
    font-family: "Lato", Arial, sans-serif;
  }
  .stage {
    position: relative;
    width: 1200px;
    height: 895px;
  }
  .card {
    position: absolute;
    left: 320px;
    width: 560px;
    height: 320px;
    background: var(--paper);
    box-shadow: 0 6px 18px rgba(0,0,0,0.18);
    overflow: hidden;
  }
  .card-front { top: 85px; }
  .card-back { top: 490px; }

  .brand-name {
    position: absolute;
    top: 100px;
    left: 0;
    width: 100%;
    text-align: center;
    font-family: "Montserrat", "Lato", sans-serif;
    font-weight: 600;
    font-size: 58px;
    letter-spacing: 1px;
    color: var(--teal);
  }
  .tagline {
    position: absolute;
    top: 205px;
    left: 0;
    width: 100%;
    text-align: center;
    font-size: 16px;
    letter-spacing: 2.5px;
    color: var(--ink);
  }

  .back-art {
    position: absolute;
    inset: 0;
  }
  .holder-name {
    position: absolute;
    left: 30px;
    top: 196px;
    margin: 0;
    font-size: 25px;
    font-weight: 700;
    color: var(--teal);
  }
  .contact-list {
    position: absolute;
    left: 30px;
    top: 240px;
    margin: 0;
    padding: 0;
    list-style: none;
    font-size: 15px;
    color: var(--brown);
  }
  .contact-list li {
    display: flex;
    align-items: center;
    gap: 10px;
    height: 24px;
  }
  .contact-list svg {
    width: 14px;
    height: 14px;
    flex: none;
  }
  .promo {
    position: absolute;
    right: 26px;
    top: 186px;
    font-size: 15px;
    font-weight: 700;
    color: var(--brown);
  }
  .promo-free {
    color: var(--teal);
    font-size: 18px;
  }
</style>
</head>
<body>
<main class="stage">
  <section class="card card-front" aria-label="Card front">
    <div class="brand-name">NeedleNook</div>
    <div class="tagline">Refresh, Restore, Rejuvenate</div>
  </section>

  <section class="card card-back" aria-label="Card back">
    <svg class="back-art" viewBox="0 0 560 320" width="560" height="320">
      <path class="band-teal" d="M0,0 H560 V150 Q330,180 0,8 Z" fill="var(--teal)"/>
      <path class="band-swoosh" d="M0,14 Q320,190 560,156 Q320,200 0,44 Z" fill="var(--brown)"/>
      <rect class="motif-area" x="385" y="18" width="140" height="125" rx="10"
            fill="var(--teal-soft)" role="img" aria-label="Leaf and needle motif"/>
    </svg>

    <h1 class="holder-name">Coral Haskins, MAC, L.Ac.</h1>

    <ul class="contact-list">
      <li>
        <svg viewBox="0 0 14 14" aria-hidden="true"><rect x="3" y="1" width="8" height="12" rx="1.5" fill="none" stroke="var(--teal)" stroke-width="1.6"/><circle cx="7" cy="10.8" r="0.9" fill="var(--teal)"/></svg>
        <span>612-555-0193</span>
      </li>
      <li>
        <svg viewBox="0 0 14 14" aria-hidden="true"><rect x="1" y="3" width="12" height="8.5" rx="1" fill="var(--teal)"/><path d="M1.5,3.5 L7,8 L12.5,3.5" fill="none" stroke="#fff" stroke-width="1.2"/></svg>
        <span>coral.haskins@needlenook-example.com</span>
      </li>
      <li>
        <svg viewBox="0 0 14 14" aria-hidden="true"><circle cx="7" cy="7" r="5.8" fill="none" stroke="var(--teal)" stroke-width="1.4"/><ellipse cx="7" cy="7" rx="2.5" ry="5.8" fill="none" stroke="var(--teal)" stroke-width="1.1"/><path d="M1.2,7 H12.8" stroke="var(--teal)" stroke-width="1.1"/></svg>
        <span>www.needlenook-example.com</span>
      </li>
    </ul>

    <div class="promo">first session <span class="promo-free">free</span></div>
  </section>
</main>
</body>
</html>
```